Website for Nonprofit for kids whose parents have been wounded

We need a web design for a nonprofit that serves children who have been severely burned as well as those whose parents have been wounded during military service. We will be based out of hospitals and will need a format that will encourage trust, safety, and respect. We are stick with a lot of red white and blue. We will also be looking to have a space for donations.

Target Market(s)

Kids and parents of military veterans

Industry/Entity Type

Non Profit

Number of Pages Required

5+ page

Font styles to use
Serif
Decorative

Colors
ec1f27
ffffff
0255a3

Requirements
Must have
• Be both appealing to children and adults. Create a reputable face for our organization. We need an area for donations.
Nice to have
• Something unique

```html
<!DOCTYPE html>
<html lang="en">
<head>
<meta charset="utf-8">
<title>Kinship Shield Foundation</title>
<link href="https://fonts.googleapis.com/css2?family=Cinzel:wght@400;600;700&family=Open+Sans:wght@400;600&display=swap" rel="stylesheet">
<style>
:root{
  --red:#c3161f;
  --red-dark:#9e0f17;
  --blue:#0255a3;
  --ink:#333;
  --muted:#777;
  --band:#ececec;
  --footer:#232323;
  --white:#fff;
}
*{box-sizing:border-box;margin:0;padding:0}
html,body{width:753px;height:1200px;overflow:hidden;background:var(--white)}
body{font-family:"Open Sans",Arial,sans-serif;color:var(--ink);position:relative}
.serif{font-family:"Cinzel",Georgia,serif}
.abs{position:absolute}

/* header */
.site-header{position:absolute;left:0;top:0;width:753px;height:100px;background:var(--white)}
.brand{position:absolute;left:63px;top:30px;display:flex;align-items:center;gap:8px}
.brand-dot{width:30px;height:30px;border-radius:50%;background:var(--blue)}
.brand-name{font-family:"Cinzel",Georgia,serif;font-size:20px;font-weight:600;color:var(--blue);letter-spacing:1px}
.phone{position:absolute;right:63px;top:32px;font-family:"Cinzel",Georgia,serif;font-size:15px;color:#444;letter-spacing:.5px}
.main-nav{position:absolute;left:252px;top:68px;display:flex;gap:0}
.main-nav a{font-family:"Cinzel",Georgia,serif;font-size:11.5px;color:#555;text-decoration:none;margin-right:36px;white-space:nowrap}
.main-nav a.active{color:var(--red)}

/* hero */
.hero{position:absolute;left:0;top:100px;width:753px;height:310px;overflow:hidden}
.hero-photo{position:absolute;inset:0;background:linear-gradient(90deg,#4d3f3b 0%,#7c6760 35%,#9d8c86 60%,#c9c0bb 100%)}
.hero-shade{position:absolute;inset:0;background:rgba(0,0,0,.28)}
.hero-kicker{position:absolute;top:110px;width:100%;text-align:center;color:var(--white);font-family:"Cinzel",Georgia,serif;font-size:19px;letter-spacing:1px}
.hero-title{position:absolute;top:136px;width:100%;text-align:center;color:var(--white);font-family:"Cinzel",Georgia,serif;font-size:44px;font-weight:600;letter-spacing:2px}
.btn{display:inline-block;background:var(--red);color:var(--white);font-family:"Cinzel",Georgia,serif;font-size:11px;padding:8px 14px;text-decoration:none}
.hero .btn{position:absolute;left:327px;top:200px}
.hero-dots{position:absolute;top:265px;left:0;width:100%;display:flex;justify-content:center;gap:7px}
.hero-dots span{width:6px;height:6px;border-radius:50%;background:rgba(255,255,255,.55)}
.hero-dots span.on{background:var(--white)}

/* welcome */
.welcome-photo{left:63px;top:452px;width:208px;height:163px;background:linear-gradient(160deg,#6e7b6a,#a59a8a 55%,#3d4f79)}
.section-title{font-family:"Cinzel",Georgia,serif;color:var(--red);font-weight:400}
.welcome-title{left:289px;top:450px;font-size:20px}
.body-copy{font-size:8.5px;line-height:1.55;color:var(--muted)}
.welcome-copy{left:289px;top:484px;width:183px}
.body-copy p{margin-bottom:8px}
.read-more{font-size:8px;color:var(--red);text-decoration:none}
.welcome-more{left:289px;top:606px}

.donate{left:490px;top:434px;width:200px;height:214px;background:var(--red);box-shadow:0 6px 10px rgba(0,0,0,.25);padding:12px 15px}
.donate h2{font-family:"Cinzel",Georgia,serif;color:var(--white);font-weight:400;font-size:20px;margin-bottom:12px}
.field{display:block;width:170px;height:20px;background:var(--white);margin-bottom:8px;font-size:8px;color:#999;padding:5px 6px}
.field.select{display:flex;justify-content:space-between}
.submit{display:inline-block;background:#2b2b2b;color:var(--white);font-size:8px;padding:4px 9px}

/* services */
.services{left:0;top:658px;width:753px;height:270px;background:var(--band)}
.services-title{position:absolute;top:20px;width:100%;text-align:center;font-size:20px}
.card{position:absolute;top:62px;height:178px}
.card-photo{height:133px}
.card-label{height:45px;background:var(--red);color:var(--white);font-family:"Cinzel",Georgia,serif;font-size:17px;padding:10px 12px;box-shadow:0 5px 8px rgba(0,0,0,.2)}
.card.c1{left:63px;width:200px}
.card.c2{left:276px;width:201px}
.card.c3{left:485px;width:205px}
.c1 .card-photo{background:linear-gradient(150deg,#5f7d3e,#a4b37c 60%,#c9c6b9)}
.c2 .card-photo{background:linear-gradient(150deg,#6b4c3c,#a57a63 55%,#3e3a3d)}
.c3 .card-photo{background:linear-gradient(150deg,#7c8a6c,#4f5b45 55%,#9aa6b2)}

/* mission & camps */
.mission-title{left:63px;top:957px;font-size:19px}
.mission-photo{left:63px;top:994px;width:193px;height:111px;background:linear-gradient(120deg,#2a2a2a,#6a6a6a 55%,#b2b2b2)}
.mission-copy{left:271px;top:992px;width:200px}
.mission-more{left:271px;top:1093px}
.camps-title{left:485px;top:957px;font-size:19px}
.arrows{left:668px;top:961px;display:flex;gap:8px}
.camp-photo{left:485px;top:997px;width:62px;height:50px;background:linear-gradient(140deg,#5c5a3e,#8b8458)}
.camp-name{left:557px;top:995px;font-family:"Cinzel",Georgia,serif;color:var(--red);font-size:13px}
.camp-date{left:557px;top:1013px;font-size:7.5px;color:#999}
.camp-copy{left:557px;top:1027px;width:133px}
.camp-more{left:557px;top:1093px}

/* footer */
.site-footer{left:0;top:1142px;width:753px;height:58px;background:var(--footer)}
.foot-nav{position:absolute;left:63px;top:14px;display:flex;gap:24px}
.foot-nav a{font-size:8px;color:#ccc;text-decoration:none}
.copyright{position:absolute;left:63px;top:34px;font-size:7px;color:#888}
.social{position:absolute;left:605px;top:18px;display:flex;gap:5px}
.social span{width:17px;height:17px;border-radius:50%;background:#d8d8d8}
</style>
</head>
<body>

<header class="site-header">
  <div class="brand"><span class="brand-dot"></span><span class="brand-name">K.S.F.</span></div>
  <div class="phone">CALL US: (555) 014 2468</div>
  <nav class="main-nav">
    <a class="active" href="#">Home</a>
    <a href="#">Our camps</a>
    <a href="#">Our mission</a>
    <a href="#">How to apply</a>
    <a href="#">Contact us</a>
  </nav>
</header>

<section class="hero">
  <div class="hero-photo" role="img" aria-label="Photo of a soldier holding a smiling child"></div>
  <div class="hero-shade"></div>
  <div class="hero-kicker">We serve children wounded during</div>
  <h1 class="hero-title">MILITARY SERVICE</h1>
  <a class="btn" href="#">Donate Now</a>
  <div class="hero-dots"><span class="on"></span><span></span><span></span></div>
</section>

<div class="abs welcome-photo" role="img" aria-label="Photo of a young boy in a military cap holding a flag"></div>
<h2 class="abs section-title welcome-title">Welcome to KSF</h2>
<div class="abs body-copy welcome-copy">
  <p>We stand beside children whose families carry the weight of service, offering care, camps and comfort in hospitals across the country.</p>
  <p>Our volunteers, nurses and counselors work together so every child feels safe, heard and respected while a parent heals.</p>
</div>
<a class="abs read-more welcome-more" href="#">Read more</a>

<form class="abs donate">
  <h2>Donate Now</h2>
  <span class="field">Name</span>
  <span class="field">Email</span>
  <span class="field">Phone</span>
  <span class="field select"><span>Amount</span>
    <svg width="8" height="8" viewBox="0 0 8 8"><path d="M1 2.5 4 5.5 7 2.5" fill="none" stroke="#999" stroke-width="1.2"/></svg></span>
  <span class="submit">Submit</span>
</form>

<section class="abs services">
  <h2 class="section-title services-title">Our Services</h2>
  <div class="card c1"><div class="card-photo" role="img" aria-label="Photo of a child in a wheelchair outdoors"></div><div class="card-label">wounded</div></div>
  <div class="card c2"><div class="card-photo" role="img" aria-label="Photo of a parent hugging a child"></div><div class="card-label">RED LINE</div></div>
  <div class="card c3"><div class="card-photo" role="img" aria-label="Photo of soldiers greeting families"></div><div class="card-label">Other injuries</div></div>
</section>

<h2 class="abs section-title mission-title">Our mission</h2>
<div class="abs mission-photo" role="img" aria-label="Black and white photo of a thoughtful child"></div>
<div class="abs body-copy mission-copy">
  <p>Each year we bring hundreds of children together for days of play, learning and friendship with others who understand.</p>
  <p>Through hospital programs and family support, we help kids rebuild confidence and keep hope close at home.</p>
</div>
<a class="abs read-more mission-more" href="#">Read more</a>

<h2 class="abs section-title camps-title">Our camps</h2>
<div class="abs arrows">
  <svg width="7" height="10" viewBox="0 0 7 10"><path d="M6 1 2 5 6 9" fill="none" stroke="#555" stroke-width="1.6"/></svg>
  <svg width="7" height="10" viewBox="0 0 7 10"><path d="M1 1 5 5 1 9" fill="none" stroke="#555" stroke-width="1.6"/></svg>
</div>
<div class="abs camp-photo" role="img" aria-label="Photo of children at an outdoor camp"></div>
<div class="abs camp-name">Field Camp</div>
<div class="abs camp-date">June 2015</div>
<div class="abs body-copy camp-copy"><p>A week of outdoor fun, games and teamwork for children of army families.</p></div>
<a class="abs read-more camp-more" href="#">Read more</a>

<footer class="abs site-footer">
  <nav class="foot-nav">
    <a href="#">Home</a><a href="#">Our camps</a><a href="#">Our mission</a><a href="#">How to apply</a><a href="#">Contact us</a>
  </nav>
  <div class="copyright">© 2015 Kinship Shield Inc. All rights reserved</div>
  <div class="social"><span></span><span></span><span></span><span></span><span></span></div>
</footer>

</body>
</html>
```